Kelvo Auto - help to get me noticed

We not long ago tasked Pixel Harbour to design a logo for my business. I'm happy with the result so would like to have a business card designed as a follow up.

It's an Automotive service and repair business that offers the following -
- Servicing
- General repairs
- Brakes
- Detailing
- Integrity

Kelvo Automotive
Dallin Mereth
0471 926 317

Target Market(s)

Everyday people with the ability to reach out to corporate customers also.

Industry/Entity Type

Automotive

Contact Information for Business Card

Black card, logo, name and phone number on front. Other details on back of card.

```html
<!DOCTYPE html>
<html lang="en">
<head>
<meta charset="utf-8">
<title>Kelvo Automotive – Business Card</title>
<link rel="stylesheet" href="https://fonts.googleapis.com/css2?family=Oswald:wght@500;600&family=Open+Sans:wght@400&display=swap">
<style>
  :root {
    --backdrop: #1c1c1d;
    --card: #1a1a1b;
    --card-edge: #2a2a2b;
    --green: #7cbf35;
    --green-deep: #4e9a2a;
    --white: #f2f2f2;
    --muted: #bdbdbd;
    --rule: #4a4a4a;
  }
  * { margin: 0; padding: 0; box-sizing: border-box; }
  html, body {
    width: 1200px; height: 900px; overflow: hidden;
    background: var(--backdrop);
  }
  .canvas {
    position: relative; width: 1200px; height: 900px;
    display: flex; flex-direction: column; align-items: center; justify-content: center;
    gap: 56px;
  }
  .card {
    position: relative; width: 600px; height: 340px;
    background: var(--card);
    border-radius: 22px;
    box-shadow: 0 0 0 1px var(--card-edge), 0 18px 40px rgba(0,0,0,0.45);
    overflow: hidden;
  }

  /* Front */
  .card-front { display: flex; align-items: center; justify-content: center; gap: 26px; }
  .brand-mark {
    font-family: "Oswald", sans-serif; font-weight: 600;
    color: var(--green); font-size: 62px; letter-spacing: 1px;
    text-transform: uppercase; line-height: 1;
  }
  .divider { width: 1px; height: 118px; background: var(--rule); }
  .holder { font-family: "Oswald", sans-serif; font-weight: 500; text-transform: uppercase; }
  .holder-name { color: var(--white); font-size: 34px; letter-spacing: 1.5px; line-height: 1.1; }
  .holder-name .accent { color: var(--green); }
  .holder-phone { color: var(--green); font-size: 26px; letter-spacing: 1.5px; margin-top: 4px; }

  /* Back */
  .card-back { padding: 30px 36px; }
  .intro {
    font-family: "Open Sans", sans-serif; font-size: 13px; color: var(--muted);
  }
  .services { list-style: none; margin-top: 22px; }
  .service {
    display: flex; align-items: center; gap: 8px; margin-bottom: 9px;
    font-family: "Oswald", sans-serif; font-weight: 500; font-size: 15px;
    letter-spacing: 1px; text-transform: uppercase; color: var(--white);
  }
  .tick { width: 15px; height: 15px; flex: none; }
  .back-brand {
    position: absolute; right: 40px; bottom: 32px;
    text-align: left; font-family: "Oswald", sans-serif; text-transform: uppercase;
  }
  .back-brand .brand-mark { font-size: 50px; }
  .back-brand .brand-sub {
    color: var(--white); font-weight: 500; font-size: 24px; letter-spacing: 3px; line-height: 1.1;
  }
  .back-brand .brand-phone {
    color: var(--white); font-weight: 500; font-size: 22px; letter-spacing: 2px;
  }
</style>
</head>
<body>
<main class="canvas">

  <section class="card card-front" aria-label="Business card front">
    <div class="brand-mark">Kelvo</div>
    <div class="divider"></div>
    <div class="holder">
      <div class="holder-name">Dallin Mer<span class="accent">e</span>th</div>
      <div class="holder-phone">0471 926 317</div>
    </div>
  </section>

  <section class="card card-back" aria-label="Business card back">
    <p class="intro">It's an Automotive service and repair business that offers the following -</p>
    <ul class="services">
      <li class="service"><svg class="tick" viewBox="0 0 16 16" aria-hidden="true"><rect x="1" y="3" width="11" height="11" rx="1.5" fill="none" stroke="#7cbf35" stroke-width="1.6"/><path d="M4 8.5l3 3 7-9" fill="none" stroke="#7cbf35" stroke-width="2.2" stroke-linecap="round" stroke-linejoin="round"/></svg>Servicing</li>
      <li class="service"><svg class="tick" viewBox="0 0 16 16" aria-hidden="true"><rect x="1" y="3" width="11" height="11" rx="1.5" fill="none" stroke="#7cbf35" stroke-width="1.6"/><path d="M4 8.5l3 3 7-9" fill="none" stroke="#7cbf35" stroke-width="2.2" stroke-linecap="round" stroke-linejoin="round"/></svg>General Repairs</li>
      <li class="service"><svg class="tick" viewBox="0 0 16 16" aria-hidden="true"><rect x="1" y="3" width="11" height="11" rx="1.5" fill="none" stroke="#7cbf35" stroke-width="1.6"/><path d="M4 8.5l3 3 7-9" fill="none" stroke="#7cbf35" stroke-width="2.2" stroke-linecap="round" stroke-linejoin="round"/></svg>Brakes</li>
      <li class="service"><svg class="tick" viewBox="0 0 16 16" aria-hidden="true"><rect x="1" y="3" width="11" height="11" rx="1.5" fill="none" stroke="#7cbf35" stroke-width="1.6"/><path d="M4 8.5l3 3 7-9" fill="none" stroke="#7cbf35" stroke-width="2.2" stroke-linecap="round" stroke-linejoin="round"/></svg>Detailing</li>
      <li class="service"><svg class="tick" viewBox="0 0 16 16" aria-hidden="true"><rect x="1" y="3" width="11" height="11" rx="1.5" fill="none" stroke="#7cbf35" stroke-width="1.6"/><path d="M4 8.5l3 3 7-9" fill="none" stroke="#7cbf35" stroke-width="2.2" stroke-linecap="round" stroke-linejoin="round"/></svg>Integrity</li>
    </ul>
    <div class="back-brand">
      <div class="brand-mark">Kelvo</div>
      <div class="brand-sub">Automotive</div>
      <div class="brand-phone">0471 926 317</div>
    </div>
  </section>

</main>
</body>
</html>
```